Business Card Design

I need a business card for my company i am starting. I will be providing stump grinding services. I use a motorized machine to grind stumps down under the ground so that they are out of the way and out of sight. I'm looking for my card to have maroon or dark red somewhere in the card to match my truck. I'm going to use this card to advertise and also serve as a design to wrap my truck tailgate as advertisement so i want it to match. the dark maroon color of my truck. I wouldn't mind using bright colors or color for the rest of the card or the lettering or any designs on the card. In the images i have provided i like how there are saw blades integrated into these people advertisements. I also like the illustration of the stump grinder. I also provided a picture of the actual cutting wheel or blade of the grinder.

Industry/Entity Type

Business

Contact Information for Business Card

Company Name - Oakline Stump Grinding
Phone - 407-219-5573
Email - harlow.stumpwork@quillpost.net
Name and title - Thomas Harlow - Owner and operator
Company Slogan - You find them, I'll grind them

```html
<!DOCTYPE html>
<html lang="en">
<head>
<meta charset="utf-8">
<title>Oakline Stump Grinding – Business Card</title>
<link href="https://fonts.googleapis.com/css2?family=Open+Sans:wght@400;600;700&display=swap" rel="stylesheet">
<style>
  :root {
    --maroon: #7a1f2b;
    --maroon-soft: #a0404c;
    --charcoal: #333333;
    --ink: #1e1e1e;
    --paper: #ffffff;
    --backdrop: #2b2d31;
  }
  * { margin: 0; padding: 0; box-sizing: border-box; }
  html, body {
    width: 1200px; height: 864px; overflow: hidden;
    background: var(--backdrop);
    font-family: "Open Sans", Arial, sans-serif;
  }
  .card {
    position: absolute; left: 320px;
    width: 560px; height: 320px;
    background: var(--paper);
    overflow: hidden;
  }
  .card--front { top: 60px; }
  .card--back { top: 470px; }

  /* front */
  .brand {
    position: absolute; left: 0; right: 0; top: 110px;
    display: flex; justify-content: center; align-items: center; gap: 14px;
  }
  .brand__dot {
    flex: none;
    width: 54px; height: 54px; border-radius: 50%;
    background: var(--maroon);
  }
  .brand__name {
    font-weight: 700; font-size: 30px; color: var(--maroon);
    letter-spacing: .5px; white-space: nowrap;
  }
  .tagline {
    position: absolute; left: 0; right: 0; top: 225px;
    display: flex; align-items: center; gap: 10px;
  }
  .tagline__rule { flex: 1; height: 1px; background: var(--maroon-soft); opacity: .7; }
  .tagline__text {
    font-weight: 600; font-size: 17px; color: var(--ink); white-space: nowrap;
  }
  .tagline__accent { color: var(--maroon); }

  /* back */
  .back-brand {
    position: absolute; left: 48px; top: 40px;
    font-weight: 700; font-size: 30px; color: var(--maroon); white-space: nowrap;
  }
  .person { position: absolute; left: 48px; top: 140px; }
  .person__name { font-weight: 700; font-size: 19px; color: var(--maroon); }
  .person__title { font-size: 13px; color: var(--ink); }
  .contact { position: absolute; left: 48px; top: 210px; list-style: none; }
  .contact__item {
    display: flex; align-items: center; gap: 10px;
    font-size: 14px; color: var(--ink); margin-bottom: 8px; white-space: nowrap;
  }
  .contact__icon { flex: none; width: 12px; height: 12px; }
  .contact__icon--phone { fill: var(--maroon); }
  .contact__icon--mail { fill: none; stroke: var(--maroon); stroke-width: 2.4; stroke-linejoin: round; }
  .accent-disc {
    position: absolute; right: -150px; top: 10px;
    width: 300px; height: 300px; border-radius: 50%;
    background: var(--maroon);
  }
</style>
</head>
<body>
  <section class="card card--front">
    <div class="brand">
      <span class="brand__dot"></span>
      <span class="brand__name">Oakline Stump Grinding</span>
    </div>
    <div class="tagline">
      <span class="tagline__rule"></span>
      <span class="tagline__text">You find them, <span class="tagline__accent">I'll grind them</span></span>
      <span class="tagline__rule"></span>
    </div>
  </section>

  <section class="card card--back">
    <div class="back-brand">Oakline Stump Grinding</div>
    <div class="person">
      <div class="person__name">Thomas Harlow</div>
      <div class="person__title">Owner &amp; Operator</div>
    </div>
    <ul class="contact">
      <li class="contact__item">
        <svg class="contact__icon contact__icon--phone" viewBox="0 0 24 24" aria-hidden="true"><path d="M6.6 10.8a15.1 15.1 0 0 0 6.6 6.6l2.2-2.2c.3-.3.7-.4 1-.2 1.1.4 2.3.6 3.6.6.6 0 1 .4 1 1V20c0 .6-.4 1-1 1A17 17 0 0 1 3 4c0-.6.4-1 1-1h3.5c.6 0 1 .4 1 1 0 1.3.2 2.5.6 3.6.1.3 0 .7-.2 1z"/></svg>
        407-219-5573
      </li>
      <li class="contact__item">
        <svg class="contact__icon contact__icon--mail" viewBox="0 0 24 24" aria-hidden="true"><rect x="2" y="5" width="20" height="14"/><path d="M2 5l10 7 10-7"/></svg>
        harlow.stumpwork@quillpost.net
      </li>
    </ul>
    <div class="accent-disc"></div>
  </section>
</body>
</html>
```